Letterhead to Prospective Clients

Create a letterhead (word & canva) that I will use to send letters to prospective clients and also include the Coralwood Estate Partners Logo, My Contact Details and Interchangeable "Suburb". Use the same font and colour pallete

Maris Dulworth | "Suburb" Specialist - Redlands & Surrounds
Mobile: 0417 862 095
Email: MD@CoralwoodEstatePartners.com.au

```html
<!DOCTYPE html>
<html lang="en">
<head>
<meta charset="utf-8">
<title>Coralwood Estate Partners — Letterhead</title>
<link rel="stylesheet" href="https://fonts.googleapis.com/css2?family=Arimo:wght@400&family=Open+Sans:wght@400&display=swap">
<style>
  :root {
    --paper: #f7f4f5;
    --navy: #1d2a4a;
    --ink: #3a3a3a;
    --body-ink: #4a4a4a;
    --sig-tone: #c9ccd6;
  }
  html, body {
    margin: 0;
    padding: 0;
    width: 942px;
    height: 1200px;
    overflow: hidden;
    background: var(--paper);
  }
  .letterhead {
    position: relative;
    width: 942px;
    height: 1200px;
    background: var(--paper);
    font-family: "Arimo", Arial, sans-serif;
    color: var(--body-ink);
  }
  .brand {
    position: absolute;
    left: 78px;
    top: 112px;
    display: flex;
    align-items: center;
    gap: 12px;
    font-family: "Arimo", Arial, sans-serif;
    font-weight: 400;
    font-size: 25px;
    letter-spacing: 1px;
    color: var(--navy);
  }
  .brand-dot {
    width: 14px;
    height: 14px;
    border-radius: 50%;
    background: var(--navy);
  }
  .contact {
    position: absolute;
    left: 603px;
    top: 102px;
    margin: 0;
    padding: 0;
    list-style: none;
    font-family: "Open Sans", Arial, sans-serif;
    font-size: 14px;
    line-height: 17.5px;
    color: var(--ink);
  }
  .contact li {
    display: flex;
    align-items: center;
    gap: 7px;
  }
  .contact svg {
    width: 12px;
    height: 12px;
    fill: var(--navy);
    flex: none;
  }
  .salutation {
    position: absolute;
    left: 64px;
    top: 286px;
    margin: 0;
    font-size: 25px;
    font-weight: 400;
    color: var(--ink);
  }
  .letter-body {
    position: absolute;
    left: 64px;
    top: 362px;
    width: 816px;
  }
  .letter-body p {
    margin: 0 0 20.5px;
    font-size: 14.4px;
    line-height: 20.5px;
    text-align: justify;
  }
  .closing {
    position: absolute;
    left: 64px;
    top: 794px;
    margin: 0;
    font-size: 14.4px;
  }
  .signature {
    position: absolute;
    left: 74px;
    top: 872px;
    width: 124px;
    height: 48px;
    background: linear-gradient(90deg, var(--paper), var(--sig-tone), var(--paper));
  }
  .signatory {
    position: absolute;
    left: 75px;
    top: 938px;
  }
  .signatory-name {
    display: block;
    font-size: 20px;
    color: var(--ink);
  }
  .signatory-role {
    display: block;
    margin-top: 4px;
    font-size: 15px;
    color: var(--ink);
  }
</style>
</head>
<body>
<main class="letterhead">
  <header>
    <div class="brand"><span class="brand-dot"></span>Coralwood Estate Partners</div>
    <ul class="contact">
      <li>
        <svg viewBox="0 0 12 12" aria-hidden="true"><path d="M3 0h6a1 1 0 0 1 1 1v10a1 1 0 0 1-1 1H3a1 1 0 0 1-1-1V1a1 1 0 0 1 1-1zm0 1.5v8h6v-8z"/></svg>
        0417 862 095
      </li>
      <li>
        <svg viewBox="0 0 12 12" aria-hidden="true"><path d="M0 2h12v8H0zM1 3v.4l5 3.2 5-3.2V3z"/></svg>
        MD@CoralwoodEstatePartners.com.au
      </li>
      <li>
        <svg viewBox="0 0 12 12" aria-hidden="true"><circle cx="6" cy="6" r="6"/><path d="M4 3c1 0 2 1 1.5 2S3 5.5 3.5 7 5 9 4.5 10.5M8 2.5c-.5 1 .5 2 1.5 2M7.5 8c1 0 1.5 1 1 2" stroke="#f7f4f5" stroke-width="1" fill="none"/></svg>
        www.CoralwoodEstatePartners.com.au
      </li>
    </ul>
  </header>

  <h1 class="salutation">Dear Mr. Smith,</h1>

  <section class="letter-body">
    <p>Lorem ipsum dolor sit amet, consectetur adipiscing elit. Donec orci purus, luctus vitae dignissim eu, iaculis sed purus. Vivamus faucibus, ipsum nec aliquet viverra, leo mauris condimentum ligula, sit amet sagittis enim ligula quis arcu. Nam egestas tortor id nisi porttitor mattis. In tortor ante, ultricies in suscipit a, tempus non massa. Vivamus et auctor mi. Fusce vel massa nulla. Phasellus nec eros mauris, et scelerisque orci.</p>
    <p>Donec malesuada orci vitae nulla accumsan porta a id massa. Quisque accumsan iaculis magna sit amet fringilla. Maecenas consequat, magna eget tincidunt semper, odio nibh rutrum mi, id feugiat ante nisi eu risus. Vestibulum nunc orci, rhoncus a placerat in, ultricies in mi. Cras mattis varius eros, vel fringilla nisi suscipit eget. Quisque scelerisque sagittis nulla at porttitor.</p>
    <p>Sed id augue vitae urna euismod commodo aliquet a quam. Pellentesque arcu velit, cursus et malesuada ut, consequat et diam. Nullam erat sem, rhoncus id ullamcorper vitae, rhoncus et arcu. In ultricies ultricies nulla, ut rutrum nisi iaculis at. Donec eu magna a metus ornare faucibus. Fusce aliquet faucibus ultricies. Morbi semper, est id tincidunt gravida, sem arcu adipiscing lacus, ac bibendum nulla leo eu purus. Quisque nec diam sed risus consectetur a ccumsan quis quis nibh. Vestibulum id purus lorem.</p>
    <p>It is a long established fact that a reader will be distracted by the readable content of a page when looking at its layout. The point of using Lorem Ipsum is that it has a more-or-less normal distribution of letters, as opposed to using 'Content here, content here', making it look like readable English. Many desktop publishing packages</p>
  </section>

  <p class="closing">Sincerely,</p>
  <div class="signature" role="img" aria-label="Handwritten signature of Maris Dulworth"></div>
  <div class="signatory">
    <span class="signatory-name">Maris Dulworth</span>
    <span class="signatory-role">"Suburb" Specialist - Redlands &amp; Surrounds</span>
  </div>
</main>
</body>
</html>
```